Need UI design of one scene of a word game app

We need your help to design a game play scene of a word game app for vornel shopdeck. This is just one scene of the whole app. We may need design of more scenes of the game in the future.

Here is the list of items we need:
1.The overall UI design of this scene and the pop-up window within the scene.
2.The button designs of this scene.
3.One ice drawing around the frame.
4.One lightning animation (with several images) around the button.
5.This scene will support both torvex and lumbra. So the screen size will be 640x1196 and 1536x2048.

Please refer to the pdf file attached for details.

Thank you.

```html
<!DOCTYPE html>
<html lang="en">
<head>
<meta charset="utf-8">
<title>Word Game – Play Scene</title>
<link rel="stylesheet" href="https://fonts.googleapis.com/css2?family=Roboto:wght@300;400;700;900&display=swap">
<style>
  :root {
    --sky: #cdeef8;
    --ice-edge: #e9f8fd;
    --ice-rim: #9fd9ec;
    --board: #000000;
    --panel: #ffffff;
    --teal: #2a9fc4;
    --ink: #111111;
    --btn-dark: #3a3a3a;
    --btn-dark-edge: #1e1e1e;
    --fire: #e02b1f;
    --fire-dark: #a8170f;
    --frost: #7fd3ec;
    --frost-dark: #48b4d6;
    --bolt: #f2a20c;
    --bolt-dark: #c67a00;
    --ad-band: #000000;
    --ad-text: #7a7a7a;
  }
  * { margin: 0; padding: 0; box-sizing: border-box; }
  html, body { width: 1200px; height: 2240px; overflow: hidden; }
  body {
    position: relative;
    background: var(--sky);
    font-family: "Roboto", Arial, sans-serif;
  }
  .game-scene { position: absolute; left: 0; top: 0; width: 1200px; height: 1904px; background: var(--sky); }

  .play-board {
    position: absolute; left: 28px; top: 20px; width: 940px; height: 1630px;
    background: var(--board);
    border-radius: 36px;
    border: 14px solid var(--ice-edge);
    box-shadow: 0 0 0 6px var(--ice-rim), 0 0 30px 8px rgba(255,255,255,0.8);
  }

  .status-panel {
    position: absolute; left: 996px; top: 32px; width: 176px; height: 690px;
    background: var(--panel); border-radius: 22px;
    box-shadow: 0 0 0 5px var(--ice-edge);
    text-align: center;
  }
  .pause-button {
    position: absolute; left: 22px; top: 48px; width: 132px; height: 136px;
    background: linear-gradient(#4a4a4a, var(--btn-dark));
    border: 4px solid var(--btn-dark-edge); border-radius: 16px;
    display: flex; align-items: center; justify-content: center; gap: 20px;
  }
  .pause-button span { width: 18px; height: 62px; background: #fff; border-radius: 4px; }
  .stat-label { position: absolute; left: 0; width: 100%; color: var(--teal); font-size: 40px; font-weight: 400; }
  .stat-value { position: absolute; left: 0; width: 100%; color: var(--ink); font-size: 72px; font-weight: 900; }

  .power-up { position: absolute; left: 1000px; width: 176px; text-align: center; }
  .power-up .tile {
    width: 176px; height: 178px; border-radius: 16px;
    display: flex; align-items: center; justify-content: center;
    box-shadow: 0 0 0 5px var(--ice-edge);
  }
  .power-up .count { margin-top: 22px; font-size: 40px; font-weight: 700; color: var(--teal); }
  .fire .tile { background: linear-gradient(#f04335, var(--fire)); border: 4px solid var(--fire-dark); }
  .frost .tile { background: linear-gradient(#a6e4f5, var(--frost)); border: 4px solid var(--frost-dark); }
  .bolt .tile { background: linear-gradient(#ffbb2a, var(--bolt)); border: 4px solid var(--bolt-dark); }

  .word-bar {
    position: absolute; left: 32px; top: 1688px; width: 1140px; height: 180px;
    background: var(--panel); border-radius: 26px;
    box-shadow: 0 0 0 5px var(--ice-edge);
  }
  .word-bar .current-word {
    position: absolute; left: 90px; width: 700px; top: 0; height: 180px;
    display: flex; align-items: center; justify-content: center;
    font-size: 72px; font-weight: 900; letter-spacing: 40px; color: var(--ink);
  }
  .clear-button {
    position: absolute; right: 18px; top: 20px; width: 292px; height: 140px;
    background: linear-gradient(#525252, var(--btn-dark));
    border: 4px solid var(--btn-dark-edge); border-radius: 16px;
    color: #fff; font-size: 62px; font-weight: 700;
    display: flex; align-items: center; justify-content: center;
  }

  .ad-band {
    position: absolute; left: 0; top: 1904px; width: 1200px; height: 336px;
    background: var(--ad-band);
    display: flex; align-items: center; justify-content: center;
    color: var(--ad-text); font-size: 76px; font-weight: 300;
  }
</style>
</head>
<body>
  <main class="game-scene">
    <div class="play-board" role="img" aria-label="Game board framed with ice"></div>

    <aside class="status-panel">
      <div class="pause-button" aria-label="Pause"><span></span><span></span></div>
      <div class="stat-label" style="top:318px">Letter</div>
      <div class="stat-value" style="top:362px">1</div>
      <div class="stat-label" style="top:462px">Level</div>
      <div class="stat-value" style="top:520px">1</div>
    </aside>

    <div class="power-up fire" style="top:784px">
      <div class="tile">
        <svg width="90" height="100" viewBox="0 0 90 100" aria-label="Fire">
          <path d="M45 6c8 18 30 28 30 56a30 30 0 0 1-60 0c0-14 8-22 14-28 0 10 4 16 10 18-4-18 2-34 6-46z" fill="#fff"/>
          <path d="M45 54c6 8 14 12 14 24a14 14 0 0 1-28 0c0-8 6-12 8-18 2 6 4 8 6 8z" fill="var(--fire)"/>
        </svg>
      </div>
      <div class="count">X1</div>
    </div>

    <div class="power-up frost" style="top:1082px">
      <div class="tile">
        <svg width="96" height="96" viewBox="0 0 96 96" aria-label="Freeze">
          <g stroke="#fff" stroke-width="9" stroke-linecap="round" fill="none">
            <path d="M48 8v80M13 28l70 40M13 68l70-40"/>
            <path d="M36 14l12 12 12-12M36 82l12-12 12 12"/>
          </g>
        </svg>
      </div>
      <div class="count">X1</div>
    </div>

    <div class="power-up bolt" style="top:1378px">
      <div class="tile">
        <svg width="70" height="100" viewBox="0 0 70 100" aria-label="Lightning">
          <path d="M42 4L10 56h22l-8 40 36-56H38z" fill="#fff"/>
        </svg>
      </div>
      <div class="count">X1</div>
    </div>

    <section class="word-bar">
      <div class="current-word">WORD</div>
      <div class="clear-button">CLEAR</div>
    </section>
  </main>

  <footer class="ad-band">Advertisement</footer>
</body>
</html>
```